Pause Your Day And Browse- PYDAB poster

I am the Vice President of Advocacy for the Coastal School Bookkeepers Guild. I am looking to have a set of posters made for PYDAB (Pause Your Day and Browse) October 23. PYDAB is a time when all school children in BC are encouraged to Pause Your Day and Browse for 15-20 minutes at some point in their day.

I would like to get a set of 2 digital posters designed (if possible it would be nice to have the option to print to both 11 x 17 and 8.5 x 11 paper). We need a poster that is high school (Grade 8-12) appropriate and one that is elementary (Grade k-7) appropriate. Both posters need to be replicated in French. All posters need to have the PEWU logo on them as well as the Coastal School Bookkeepers Guild Logo.

Here is a link to last year's successful design http://pewu-sample.ca/csbg/info/outreach.html
There are two additional samples in the uploaded files section.

Each poster needs to have the following information:

-Pause Your Day and Browse (PYDAB)
- The date Monday, October 23, 2017
-the logo for the PEWU (attached)
-the logo for the CSBG (attached)- the logos do not have to be large.

Target Market(s)

Children ages 5-12 and 12-17 as well as their teachers

Industry/Entity Type

Teacher

Font styles to use
Sans Serif

Requirements
Must have
• Must have both logos- colours may be changed for either or both
Nice to have
• Clear, Bright lettering. Images of child or children enjoying reading
Should not have
• stereotypes

```html
<!DOCTYPE html>
<html lang="fr">
<head>
<meta charset="utf-8">
<title>PYDAB – Laissez Tout Tomber et Lis</title>
<link rel="stylesheet" href="https://fonts.googleapis.com/css2?family=Anton&family=Oswald:wght@500;600&display=swap">
<style>
  :root {
    --paper: #ffffff;
    --orange: #f7941d;
    --slate-blue: #44718f;
    --ink: #1f2a44;
    --mark-blue: #243f7f;
    --book-cream: #f3e6c4;
    --book-red: #ef5a57;
    --book-blue: #3e6a93;
  }
  html, body {
    margin: 0;
    padding: 0;
    width: 776px;
    height: 1200px;
    overflow: hidden;
    background: var(--paper);
  }
  .poster {
    display: block;
    width: 776px;
    height: 1200px;
  }
  .headline-pydab {
    font-family: "Anton", "Oswald", sans-serif;
    font-size: 253px;
    fill: var(--orange);
  }
  .headline-tagline {
    font-family: "Oswald", sans-serif;
    font-weight: 600;
    font-size: 76px;
    fill: var(--slate-blue);
  }
  .headline-etlis {
    font-family: "Anton", "Oswald", sans-serif;
    font-size: 300px;
    fill: var(--slate-blue);
  }
  .date-band { fill: var(--slate-blue); }
  .date-text {
    font-family: "Oswald", sans-serif;
    font-weight: 600;
    font-size: 54px;
    fill: var(--paper);
  }
  .partner-name {
    font-family: "Oswald", sans-serif;
    font-weight: 600;
    fill: var(--ink);
  }
  .partner-name--guild { font-size: 34px; }
  .partner-name--guild-full { font-size: 11px; }
  .partner-name--union { font-size: 34px; fill: var(--mark-blue); }
  .partner-square { fill: var(--orange); }
  .partner-circle { fill: var(--mark-blue); }
</style>
</head>
<body>
<svg class="poster" viewBox="0 0 776 1200" xmlns="http://www.w3.org/2000/svg">
  <defs>
    <linearGradient id="reader-tones" x1="0" y1="0" x2="0" y2="1">
      <stop offset="0" stop-color="var(--book-cream)"/>
      <stop offset="0.45" stop-color="var(--book-red)"/>
      <stop offset="1" stop-color="var(--book-blue)"/>
    </linearGradient>
  </defs>

  <!-- Guild name, top left -->
  <g class="partner partner--guild">
    <rect class="partner-square" x="66" y="60" width="28" height="28"/>
    <text class="partner-name partner-name--guild" x="102" y="88">CSBG</text>
    <text class="partner-name partner-name--guild-full" x="66" y="112">Coastal School</text>
    <text class="partner-name partner-name--guild-full" x="66" y="126">Bookkeepers Guild</text>
  </g>

  <!-- Union name, top right -->
  <g class="partner partner--union">
    <circle class="partner-circle" cx="658" cy="84" r="16"/>
    <text class="partner-name partner-name--union" x="680" y="97">PEWU</text>
  </g>

  <!-- Child reading on a stack of books (sits behind the lettering) -->
  <rect class="reader-illustration" x="180" y="228" width="155" height="350" rx="14"
        fill="url(#reader-tones)" opacity="0.85" role="img"
        aria-label="Illustration of a smiling child reading a red book while sitting on a stack of books"/>

  <!-- Main title -->
  <text class="headline-pydab" x="62" y="552" textLength="700" lengthAdjust="spacingAndGlyphs">PYDAB</text>

  <text class="headline-tagline" x="70" y="637" textLength="692" lengthAdjust="spacingAndGlyphs">Laissez Tout Tomber</text>

  <text class="headline-etlis" x="70" y="912" textLength="692" lengthAdjust="spacingAndGlyphs">ET LIS</text>

  <!-- Date band -->
  <rect class="date-band" x="63" y="933" width="700" height="66"/>
  <text class="date-text" x="413" y="988" text-anchor="middle" textLength="608" lengthAdjust="spacingAndGlyphs">Monday, October 23, 2017</text>
</svg>
</body>
</html>
```